Label Brelomo Beer Can for Exhibition promo not consumer sale

label for exhibtion promotional craft beer. I publish international trade techology magazines and after 13 years are unveiling a redesign for the magazines- new logo, new paper etc. The beer is for drinking and I am sure will get a bit of social promo within the trade.

Exhibtion Attendees, clients, readers

• Ultimately, it is 205mm wide by 87mm high. The guides in the file show the correct split for an aesthetically pleasing design that will get all the important info/branding on the front, and the legal stuff like the barcode and allergens on the back. Once done ,we will also likely need the source files too so that the correct barcode and ingredients can be dropped in
• We prefer a dorvalik can style (document 1)

```html
<!DOCTYPE html>
<html lang="en">
<head>
<meta charset="utf-8">
<title>Brelomo Hoppy Lager Ale – Can Label</title>
<link rel="stylesheet" href="https://fonts.googleapis.com/css2?family=Cinzel:wght@500;700&family=Playball&display=swap">
<style>
  :root {
    --backdrop: #f2f2f2;
    --label-white: #ffffff;
    --dot-grey: #c9c9cc;
    --gold-light: #eddcaa;
    --gold-mid: #d8c084;
    --gold-deep: #b8934a;
    --gold-rule: #c79a3c;
    --ink: #2b2723;
    --band-black: #121212;
    --name-white: #f4f4f4;
  }
  html, body {
    margin: 0;
    padding: 0;
    width: 967px;
    height: 1200px;
    overflow: hidden;
    background: var(--backdrop);
  }
  .label-canvas {
    display: block;
    width: 967px;
    height: 1200px;
  }
  .caps-line {
    font-family: "Cinzel", serif;
    font-weight: 500;
    fill: var(--ink);
    text-anchor: middle;
  }
  .style-script {
    font-family: "Playball", cursive;
    fill: var(--ink);
    font-size: 46px;
  }
  .brand-name {
    font-family: "Cinzel", serif;
    font-weight: 700;
    font-size: 74px;
    fill: var(--name-white);
    text-anchor: middle;
  }
</style>
</head>
<body>
<svg class="label-canvas" viewBox="0 0 967 1200" xmlns="http://www.w3.org/2000/svg">
  <defs>
    <linearGradient id="gold-fill" x1="0" y1="0" x2="1" y2="1">
      <stop offset="0" stop-color="var(--gold-light)"/>
      <stop offset="0.55" stop-color="var(--gold-mid)"/>
      <stop offset="1" stop-color="var(--gold-light)"/>
    </linearGradient>
    <linearGradient id="dot-fade" x1="0" y1="0" x2="0" y2="1">
      <stop offset="0" stop-color="var(--label-white)"/>
      <stop offset="1" stop-color="var(--dot-grey)"/>
    </linearGradient>
    <linearGradient id="gold-rule-fill" x1="0" y1="0" x2="1" y2="0">
      <stop offset="0" stop-color="var(--gold-deep)"/>
      <stop offset="0.5" stop-color="var(--gold-light)"/>
      <stop offset="1" stop-color="var(--gold-deep)"/>
    </linearGradient>
    <path id="arc-style" d="M352 575 Q500 455 650 575"/>
    <path id="arc-regions" d="M368 850 Q500 935 634 850"/>
  </defs>

  <!-- label sheet -->
  <rect class="label-sheet" x="312" y="250" width="378" height="780" fill="var(--label-white)"/>

  <!-- top halftone zone -->
  <rect class="halftone-zone" x="312" y="275" width="378" height="120" fill="url(#dot-fade)" role="img" aria-label="Grey halftone dot pattern fading downward"/>

  <!-- gold crest panel -->
  <path class="crest-panel" d="M314 425 L340 425 Q352 398 380 388 Q500 332 620 388 Q648 398 660 425 L688 425 L688 962 L314 962 Z"
        fill="url(#gold-fill)" stroke="var(--gold-rule)" stroke-width="5"/>
  <path class="crest-ornament" d="M322 432 L346 432 Q358 406 384 396 Q500 344 616 396 Q642 406 654 432 L680 432 L680 954 L322 954 Z"
        fill="url(#gold-fill)" opacity="0.7" role="img" aria-label="Faint vine and grape ornament pattern"/>

  <!-- copy above the band -->
  <text class="caps-line" x="500" y="432" font-size="21">ORIGINAL CONTENT</text>
  <text class="style-script"><textPath href="#arc-style" startOffset="50%" text-anchor="middle">Hoppy Lager Ale</textPath></text>
  <text class="caps-line" x="500" y="598" font-size="23">TRADE MAG</text>

  <!-- name band -->
  <rect class="name-band" x="312" y="618" width="378" height="118" fill="var(--band-black)"/>
  <text class="brand-name" x="500" y="705">Brelomo</text>

  <!-- copy below the band -->
  <text class="caps-line" x="500" y="834" font-size="23">REDESIGN 2019</text>
  <text class="caps-line" font-size="27"><textPath href="#arc-regions" startOffset="50%">APAC EMEA ROSSIA</textPath></text>

  <!-- foot band -->
  <rect class="foot-rule" x="312" y="964" width="378" height="6" fill="url(#gold-rule-fill)"/>
  <rect class="foot-band" x="312" y="970" width="378" height="55" fill="var(--band-black)"/>
</svg>
</body>
</html>
```